Sale- Bundle signs

We are looking for a design to use for Permanent SALE/Bundle deal signs. We are a natural bath products company who uses all natural ingredients to create our handmade line of natural products. We love a clean, fresh look and feel. Simple eye-catching that will be a quick glance and they will know the offer.
We would like to have something simple, eye catching that will promote sales on our different products.
Dead Sea Salt Body Scrubs
large 2 for $40
small 3 for $20
Moisturizing Wash with coconut & olive oil
2 for $20
There are several more needed but we are hoping to decide on one template before making all of the signs.
Visit our website here www.brightwillowco.com
Target Market(s)
Our store serves 70% women and the majority of our customers are 30+ years old.
Industry/Entity Type
It Company
Other font styles liked:
- Century Gothic or similar
Look and feel

```html
<!DOCTYPE html>
<html lang="en">
<head>
<meta charset="UTF-8">
<title>Brightwillow – Bundle Deals</title>
<link rel="stylesheet" href="https://fonts.googleapis.com/css2?family=Questrial&family=Poppins:wght@600&display=swap">
<style>
  :root {
    --leaf: #56803a;
    --leaf-soft: #5d8c3c;
    --lime: #a6c93a;
    --lime-light: #d6e79a;
    --paper: #ffffff;
    --offer: #e8582a;
    --ink: #111111;
  }
  html, body {
    margin: 0;
    padding: 0;
    overflow: hidden;
    background: var(--paper);
  }
  .sign {
    position: relative;
    width: 857px;
    height: 1200px;
    overflow: hidden;
    background: var(--paper);
    font-family: "Questrial", "Century Gothic", sans-serif;
  }
  .sign__backdrop {
    position: absolute;
    inset: 0;
    width: 857px;
    height: 1200px;
  }
  .brand {
    position: absolute;
    top: 40px;
    left: 0;
    width: 857px;
    text-align: center;
  }
  .brand__name {
    margin: 0;
    font-size: 104px;
    line-height: 1;
    font-weight: 400;
    color: var(--leaf);
    letter-spacing: -1px;
  }
  .brand__tagline {
    margin: 18px 0 0;
    font-size: 38px;
    line-height: 1;
    letter-spacing: 2px;
    color: var(--leaf-soft);
  }
  .product-title {
    position: absolute;
    margin: 0;
    font-weight: 400;
    color: var(--ink);
    line-height: 1;
  }
  .product-title--scrubs {
    top: 360px;
    left: 28px;
    font-size: 30px;
  }
  .product-title--wash {
    top: 710px;
    left: 500px;
    width: 300px;
    text-align: center;
    font-size: 35px;
    line-height: 51px;
  }
  .offer {
    position: absolute;
    margin: 0;
    font-family: "Poppins", "Arial", sans-serif;
    font-weight: 600;
    color: var(--offer);
    line-height: 1;
    text-align: center;
    white-space: nowrap;
  }
  .offer--size { font-size: 76px; }
  .offer--price { font-size: 98px; }
  .offer--large-qty { top: 428px; left: 45px; width: 400px; }
  .offer--large-price { top: 530px; left: 30px; width: 400px; }
  .offer--small-qty { top: 740px; left: 11px; width: 400px; }
  .offer--small-price { top: 822px; left: 17px; width: 400px; }
  .offer--wash-price { top: 968px; left: 380px; width: 460px; font-size: 102px; }
</style>
</head>
<body>
  <main class="sign">
    <svg class="sign__backdrop" viewBox="0 0 857 1200" aria-hidden="true">
      <defs>
        <linearGradient id="swoop-right" x1="0" y1="0" x2="0" y2="1">
          <stop offset="0" stop-color="var(--lime)" stop-color-fallback="#a6c93a" style="stop-color:#a6c93a"/>
          <stop offset="0.35" style="stop-color:#a6c93a"/>
          <stop offset="0.75" style="stop-color:#e4efc2"/>
          <stop offset="1" style="stop-color:#ffffff"/>
        </linearGradient>
        <linearGradient id="swoop-left" x1="0" y1="0" x2="0" y2="1">
          <stop offset="0" style="stop-color:#ffffff"/>
          <stop offset="0.3" style="stop-color:#f4f8e6"/>
          <stop offset="0.45" style="stop-color:#d6e79a"/>
          <stop offset="0.62" style="stop-color:#a6c93a"/>
          <stop offset="0.8" style="stop-color:#b7d461"/>
          <stop offset="1" style="stop-color:#ffffff"/>
        </linearGradient>
      </defs>
      <path class="swoop swoop--left" d="M0,0 L857,0 L857,190 C600,260 470,450 440,620 C410,800 340,1000 260,1200 L0,1200 Z" fill="url(#swoop-left)"/>
      <path class="swoop swoop--right" d="M857,190 C600,260 470,450 440,620 C410,800 340,1000 260,1200 L857,1200 Z" fill="url(#swoop-right)"/>
    </svg>

    <header class="brand">
      <h1 class="brand__name">brightwillow</h1>
      <p class="brand__tagline">NATURAL BATH PRODUCTS</p>
    </header>

    <h2 class="product-title product-title--scrubs">DEAD SEA SALT BODY SCRUBS</h2>
    <p class="offer offer--size offer--large-qty">Large 2</p>
    <p class="offer offer--price offer--large-price">for $40</p>
    <p class="offer offer--size offer--small-qty">Small 3</p>
    <p class="offer offer--price offer--small-price">for $20</p>

    <h2 class="product-title product-title--wash">MOISTURIZING<br>WASH WITH<br>COCONUT<br>&amp; OLIVE OIL</h2>
    <p class="offer offer--wash-price">2 for $20</p>
  </main>
</body>
</html>
```